Fruits and Vegetables distribution company needs a new eye catching website

We need to get our website up to date. Our clients will look at our website to learn about our products and services. Our design needs to be simple yet impactful to make our brand memorable to our visitors. We need to have somewhere to tell our clients about our history, products and services, our team. We can throw in a few fun facts and figures and maybe some testimonials to impress. We have 4 theme colors that we want to incorporate into the design, you can get in touch for the HEX/RGB codes. Please remember that smooth operation of any animations and interactions is very important.

```html
<!DOCTYPE html>
<html lang="en">
<head>
<meta charset="utf-8">
<title>Orchard Lane – Fruit &amp; Vegetable Distribution</title>
<link href="https://fonts.googleapis.com/css2?family=Marcellus&family=Open+Sans:ital,wght@0,400;0,600;0,700;1,400&display=swap" rel="stylesheet">
<style>
:root{
  --orange:#f5a623;
  --red:#c4172c;
  --green:#8cc63f;
  --dark:#1c1c1c;
  --text:#333;
  --muted:#666;
  --white:#fff;
  --rule:#e6e6e6;
}
*{box-sizing:border-box;margin:0;padding:0}
html,body{width:1200px;height:4500px;overflow:hidden}
body{position:relative;font-family:"Open Sans",Arial,sans-serif;color:var(--text);background:var(--white)}
.abs{position:absolute}
.serif{font-family:"Marcellus",Georgia,serif}
.btn{position:absolute;display:flex;align-items:center;justify-content:center;gap:8px;color:var(--white);font-weight:700;font-size:15px;text-transform:uppercase;letter-spacing:.3px}
.btn-orange{background:var(--orange)} .btn-green{background:var(--green)} .btn-red{background:var(--red);border-radius:24px}
.photo{position:absolute}

/* header */
.topline{top:0;left:0;width:1200px;height:6px;background:var(--orange)}
.header{top:6px;left:0;width:1200px;height:124px;background:var(--white)}
.logo{top:0;left:95px;width:195px;height:195px;border-radius:50%;background:var(--white);z-index:3;display:flex;align-items:flex-end;justify-content:center;padding-bottom:48px}
.logo span{font-family:"Marcellus",Georgia,serif;font-size:24px;color:var(--dark);letter-spacing:1px}
.phone{top:28px;left:790px;font-size:20px;font-weight:600;display:flex;align-items:center;gap:10px}
.login{top:26px;left:1004px;width:95px;height:36px;border-radius:3px;font-size:14px}
.nav{top:80px;left:448px;display:flex;gap:26px;font-size:15px;font-weight:700;color:var(--dark)}

/* hero */
.hero{top:130px;left:0;width:1200px;height:560px;background:linear-gradient(100deg,#4d6b2e 0%,#7e9a4c 35%,#b9a06a 60%,#a5432a 80%,#5d7d36 100%)}
.hero-title{top:300px;left:96px;font-size:44px;line-height:58px;color:var(--white);letter-spacing:3px;z-index:2}
.hero-text{top:432px;left:96px;width:420px;font-size:17px;font-weight:600;color:var(--white);line-height:24px;z-index:2}
.hero-btn{top:498px;left:99px;width:168px;height:48px}

/* service cards */
.card{top:732px;width:234px;height:218px}
.card .photo{top:0;left:0;width:234px;height:175px}
.card .bar{position:absolute;bottom:0;left:0;width:234px;height:43px;display:flex;align-items:center;justify-content:space-between;padding:0 14px 0 16px;color:var(--white);font-weight:700;font-size:15px}

/* welcome */
.section-title{position:absolute;left:0;width:1200px;text-align:center;font-family:"Marcellus",Georgia,serif;font-size:38px;color:var(--dark);letter-spacing:1px}
.welcome-copy{top:1112px;left:210px;width:780px;text-align:center;font-size:13px;line-height:22px;color:var(--muted)}
.welcome-copy p+p{margin-top:14px}
.video{top:1300px;left:318px;width:565px;height:310px;border:6px solid #eee}

/* categories */
.category-band{top:1797px;left:0;width:1200px;height:528px;background:var(--red)}
.category-title{top:1870px;left:0;width:1200px;text-align:center;font-size:36px;line-height:50px;color:var(--white);letter-spacing:1px}
.tile{top:2015px;width:224px;height:178px;background:var(--white);padding:8px}
.tile .photo{position:static;width:100%;height:100%}
.tile-label{position:absolute;top:2212px;width:224px;text-align:center;color:var(--white);font-weight:700;font-size:22px;letter-spacing:1px}

/* team */
.team-sub{top:2482px;left:0;width:1200px;text-align:center;font-size:14px;color:var(--muted)}
.member-card{top:2550px;left:425px;width:345px;height:272px;background:var(--white);box-shadow:0 4px 18px rgba(0,0,0,.14)}
.member{position:absolute;top:2578px;width:300px;text-align:center}
.avatar{width:124px;height:124px;border-radius:50%;margin:0 auto;border:4px solid var(--orange);padding:5px}
.avatar div{width:100%;height:100%;border-radius:50%;background:linear-gradient(#cfd6de,#6b7785)}
.member h3{margin-top:26px;font-size:17px;font-weight:700;color:var(--dark)}
.member h3 em{font-style:normal;font-weight:600;font-size:13px;margin-left:4px}
.member p{margin-top:12px;font-size:13px;line-height:20px;color:var(--muted)}

/* testimonial */
.testimonial-bg{top:2940px;left:0;width:1200px;height:610px;background:linear-gradient(90deg,#7a9a48 0%,#ece7df 22%,#f2efe9 50%,#ece7df 78%,#c85a2a 100%)}
.quote-box{top:3190px;left:198px;width:805px;height:180px;background:var(--white);border-radius:6px;box-shadow:0 4px 16px rgba(0,0,0,.15);padding:48px 50px 0;text-align:center;font-size:17px;line-height:32px;color:var(--dark)}
.quote-box .by{font-size:18px;font-weight:700;color:var(--red)}
.quote-box .by small{font-size:12px;color:var(--muted);font-weight:400}
.client{top:3130px;left:555px;width:92px;height:92px;border-radius:50%;border:4px solid var(--white);background:linear-gradient(#d8dde2,#4f5863);z-index:2}

/* fun facts */
.facts-title{top:3636px;left:99px;font-size:36px;color:var(--dark)}
.facts{top:3706px;left:99px;width:520px;list-style:none}
.facts li{position:relative;padding-left:30px;font-size:14px;line-height:21px;color:var(--muted);margin-bottom:22px}
.facts li::before{content:"";position:absolute;left:0;top:5px;width:11px;height:11px;border-radius:50%;background:var(--orange)}
.facts-frame{top:3650px;left:710px;width:442px;height:292px;border:2px solid var(--red)}
.facts-photo{top:3700px;left:662px;width:438px;height:282px;background:linear-gradient(135deg,#7e1f2a,#c2334a 45%,#e07a3a 70%,#6d8a3a)}

/* footer */
.footer{top:4080px;left:0;width:1200px;height:420px;background:var(--dark);color:#ddd}
.col{position:absolute;top:4155px;font-size:13px}
.col h4{font-size:15px;font-weight:700;color:var(--white);margin-bottom:22px}
.col ul{list-style:none}
.col li{margin-bottom:12px;display:flex;gap:12px;line-height:19px}
.col li .tri{color:#aaa;font-size:9px;margin-top:1px}
.field{width:252px;height:34px;border:1px solid #888;padding:0 8px;display:flex;align-items:center;color:var(--white);font-size:13px;margin-top:16px}
.subscribe{position:static;width:110px;height:36px;margin-top:18px;font-size:13px}
.rule{top:4392px;height:1px;background:#666;width:320px}
.socials{top:4373px;left:513px;display:flex;gap:14px}
.socials span{width:36px;height:36px;border-radius:50%;border:2px solid #ccc}
.copyright{top:4446px;left:0;width:1200px;text-align:center;font-size:13px;color:#ddd}
</style>
</head>
<body>

<div class="abs topline"></div>
<header class="abs header"></header>
<div class="abs logo"><span>Orchard Lane</span></div>
<div class="abs phone">
  <svg width="26" height="26" viewBox="0 0 24 24"><circle cx="12" cy="12" r="11" fill="none" stroke="#c4172c" stroke-width="2"/><path d="M8 6.5l2 2-1.2 1.6a7 7 0 0 0 5.1 5.1l1.6-1.2 2 2-1.4 1.6C12 17.5 6.5 12 6.4 7.9z" fill="#c4172c"/></svg>
  (+1) 555 210 4480
</div>
<div class="btn btn-green login">
  <svg width="12" height="14" viewBox="0 0 12 14"><rect x="1" y="6" width="10" height="8" fill="#fff"/><path d="M3 6V4a3 3 0 0 1 6 0v2" stroke="#fff" stroke-width="1.6" fill="none"/></svg>Login
</div>
<nav class="abs nav"><span>HOME</span><span>ABOUT US</span><span>PRODUCTS &amp; SERVICES</span><span>TEAM</span><span>TESTIMONIALS</span><span>CONTACT</span></nav>

<div class="photo hero" role="img" aria-label="Wicker basket full of tomatoes, peppers, potatoes and fresh greens on a wooden table"></div>
<h1 class="abs serif hero-title">VEGETABLES<br>DISTRIBUTION</h1>
<p class="abs hero-text">Lorem ipsum dolor sit amet consectetur adipiscing elit, sed do eiusmod tempor incididunt.</p>
<div class="btn btn-red hero-btn">Read more <span>➔</span></div>

<div class="abs card" style="left:99px"><div class="photo" role="img" aria-label="Market stall crates of produce" style="background:linear-gradient(135deg,#5a3b22,#b5532d,#7f8d3a)"></div><div class="bar" style="background:var(--orange)">AVAILABILITY GUIDES <span>➔</span></div></div>
<div class="abs card" style="left:354px"><div class="photo" role="img" aria-label="Tomatoes and vegetables at a market" style="background:linear-gradient(135deg,#6c8b33,#c73a2a,#8a2a1f)"></div><div class="bar" style="background:var(--red)">MARKET REPORTS <span>➔</span></div></div>
<div class="abs card" style="left:609px"><div class="photo" role="img" aria-label="Basket of mixed vegetables" style="background:linear-gradient(135deg,#4f7a2a,#b8893f,#a8452c)"></div><div class="bar" style="background:var(--orange)">CORE VALUES <span>➔</span></div></div>
<div class="abs card" style="left:864px"><div class="photo" role="img" aria-label="Smiling shop assistant with produce" style="background:linear-gradient(135deg,#5f7b3a,#c9a77e,#3e6a8a)"></div><div class="bar" style="background:var(--orange)">SERVICES <span>➔</span></div></div>

<h2 class="section-title" style="top:1040px">WELCOME TO ORCHARD LANE</h2>
<div class="abs welcome-copy">
  <p>Lorem ipsum dolor sit amet, consectetur adipiscing elit, sed do eiusmod tempor incididunt ut labore et dolore magna aliqua. Ut enim ad minim veniam, quis nostrud exercitation ullamco laboris nisi ut aliquip ex ea commodo consequat.</p>
  <p>Duis aute irure dolor in reprehenderit in voluptate velit esse cillum dolore eu fugiat nulla pariatur. Excepteur sint occaecat cupidatat non proident, sunt in culpa qui officia deserunt mollit anim id est laborum. Sed ut perspiciatis unde omnis iste natus error sit voluptatem accusantium doloremque laudantium, totam rem aperiam, eaque ipsa quae ab illo inventore.</p>
</div>
<div class="photo" role="img" aria-label="Blueberries" style="top:1345px;left:0;width:310px;height:200px;background:radial-gradient(ellipse at 50% 55%,#3c5a9a 0%,#2b3f74 45%,rgba(255,255,255,0) 72%)"></div>
<div class="photo" role="img" aria-label="Bunch of fresh chives" style="top:1350px;left:900px;width:300px;height:190px;background:radial-gradient(ellipse at 50% 50%,#5f9a2e 0%,#8cc63f 35%,rgba(255,255,255,0) 70%)"></div>
<div class="photo video" role="img" aria-label="Video of a colourful pile of mixed fruits" style="background:linear-gradient(135deg,#6b8a2e,#c3462a 40%,#e3a23a 60%,#7b2c4a)"></div>
<svg class="abs" style="top:1425px;left:568px" width="64" height="64" viewBox="0 0 64 64"><circle cx="32" cy="32" r="29" fill="rgba(0,0,0,.35)" stroke="#fff" stroke-width="3"/><path d="M26 20l18 12-18 12z" fill="#fff"/></svg>
<div class="btn btn-orange" style="top:1643px;left:99px;width:225px;height:47px">View all producs <span>➔</span></div>
<div class="btn btn-green" style="top:1643px;left:876px;width:224px;height:47px">Visit our shop <span>➔</span></div>

<div class="abs category-band"></div>
<h2 class="abs serif category-title">CHOOSE A CATEGORY TO SEE THE PRODUCTS<br>AND THEIR AVAILABILITY</h2>
<div class="abs tile" style="left:99px"><div class="photo" role="img" aria-label="Assorted fruits" style="background:linear-gradient(135deg,#e27b2a,#c7233a,#8cc63f)"></div></div>
<div class="abs tile" style="left:360px"><div class="photo" role="img" aria-label="Cabbages" style="background:linear-gradient(135deg,#6a3f7a,#8ab04a,#c7d99a)"></div></div>
<div class="abs tile" style="left:617px"><div class="photo" role="img" aria-label="Bunch of parsley" style="background:radial-gradient(circle,#4c8a2a,#7ab648 55%,#fff 80%)"></div></div>
<div class="abs tile" style="left:876px"><div class="photo" role="img" aria-label="Garlic bulbs" style="background:radial-gradient(circle,#e9e2d6,#c7b59a 55%,#fff 85%)"></div></div>
<div class="tile-label" style="left:99px">FRUITS</div>
<div class="tile-label" style="left:360px">VEGETABLES</div>
<div class="tile-label" style="left:617px">HERBS</div>
<div class="tile-label" style="left:876px">SPECIALTY</div>

<h2 class="section-title" style="top:2425px">MEET OUR TEAM</h2>
<p class="abs team-sub">We understand the success secrets of the world's most successful business teams.</p>
<div class="abs member-card"></div>
<div class="member" style="left:149px"><div class="avatar" role="img" aria-label="Portrait of Marcus Hale"><div></div></div><h3>MARCUS HALE,<em style="color:var(--orange)">Founder &amp; CEO</em></h3><p>Nemo enim ipsam voluptem quia voluptas sit aspern aut fugit sed quia consequuntur magni.</p></div>
<div class="member" style="left:448px"><div class="avatar" style="border-color:var(--green)" role="img" aria-label="Portrait of Lena Morrow"><div></div></div><h3>LENA MORROW,<em style="color:var(--orange)">Manager</em></h3><p>Nemo enim ipsam voluptem quia voluptas sit aspern aut fugit sed quia consequuntur magni.</p></div>
<div class="member" style="left:750px"><div class="avatar" style="border-color:var(--red)" role="img" aria-label="Portrait of Clara Vance"><div></div></div><h3>CLARA VANCE,<em style="color:var(--red)">Co-Excecutive</em></h3><p>Nemo enim ipsam voluptem quia voluptas sit aspern aut fugit sed quia consequuntur magni.</p></div>

<div class="photo testimonial-bg" role="img" aria-label="Fresh vegetables arranged around a pale wooden table"></div>
<h2 class="section-title" style="top:3055px">WHAT OUR CLIENTS SAY</h2>
<div class="abs client" role="img" aria-label="Portrait of client Owen Pryce"></div>
<div class="abs quote-box">
  <p>" Lorem ipsum dolor sit amet, consectetur adipiscing elit, sed do eiusmod tempor incididunt ut labore et dolore magna aliqua enim ad minim veniam, quis nostrud exercitation. "</p>
  <p class="by">- Owen Pryce, <small>Head Chef, Riverside Hotel</small></p>
</div>

<h2 class="abs serif facts-title">FUN FACTS ABOUT FRUITS</h2>
<ul class="abs facts">
  <li>A banana is not a fruit, it is a herb! Being easy to digest and highly nutritious, these are the first fruits offered to babies.</li>
  <li>Strawberries are the only fruit with seeds on the outside. There are 200 seeds in an average strawberry.</li>
  <li>Apples, peaches and raspberries are all members of the rose family.</li>
  <li>Pineapples are actually berries and it's ripening can be speeded up by making it stand upside down (leafy side down).</li>
</ul>
<div class="btn btn-green" style="top:3935px;left:99px;width:225px;height:46px">View all fruits fact <span>➔</span></div>
<div class="abs facts-frame"></div>
<div class="photo facts-photo" role="img" aria-label="Bowl of mixed berries and cherries"></div>

<footer class="abs footer"></footer>
<div class="col" style="left:99px"><h4>QUICK LINKS</h4><ul><li><span class="tri">▶</span>Home</li><li><span class="tri">▶</span>About Us</li><li><span class="tri">▶</span>Products</li><li><span class="tri">▶</span>Fruits &amp; Vegetables</li><li><span class="tri">▶</span>Contact Us</li></ul></div>
<div class="col" style="left:315px"><h4>RESOURCES</h4><ul><li><span class="tri">▶</span>Distribution</li><li><span class="tri">▶</span>Our Team</li><li><span class="tri">▶</span>Find Our Shop</li><li><span class="tri">▶</span>FAQ</li><li><span class="tri">▶</span>Terms Of Services</li></ul></div>
<div class="col" style="left:560px;width:230px"><h4>CONTACT US</h4><ul>
  <li><svg width="12" height="16" viewBox="0 0 12 16"><path d="M6 0a6 6 0 0 1 6 6c0 4-6 10-6 10S0 10 0 6a6 6 0 0 1 6-6z" fill="#ddd"/><circle cx="6" cy="6" r="2" fill="#1c1c1c"/></svg><span>PO Box 4821, Willow Rd, Brookfield, North State</span></li>
  <li style="margin-top:8px"><svg width="14" height="14" viewBox="0 0 24 24"><path d="M6 2l4 4-2 3a12 12 0 0 0 7 7l3-2 4 4-3 4C9 21 3 15 2 5z" fill="#ddd"/></svg><span>(+1) 555 210 4480</span></li>
  <li style="margin-top:8px"><svg width="14" height="12" viewBox="0 0 14 12"><rect width="14" height="12" fill="#ddd"/><path d="M0 0l7 6 7-6" stroke="#1c1c1c" fill="none"/></svg><span>info@orchardlane.com</span></li>
</ul></div>
<div class="col" style="left:845px;width:260px"><h4>NEWSLETTER SUBSCRIPTION</h4><p style="line-height:19px">Register your Email Address to get more Information about us</p><div class="field">Email Address</div><div class="btn btn-green subscribe">Subscribe</div></div>
<div class="abs rule" style="left:180px"></div>
<div class="abs rule" style="left:700px"></div>
<div class="abs socials"><span></span><span></span><span></span><span></span></div>
<p class="abs copyright">Copyrights © 2018 Orchard Lane. &nbsp;All Rights Reserved &nbsp; | &nbsp; Privacy Policy.</p>

</body>
</html>
```